Veltrona5 website

Need to create a website for my business

Target Market(s)

Food ingredient companies, B2B

Industry/Entity Type

Food technology, food ingredients

Coding

Coded - Design and coding required

Number of Pages Required

2 page

Requirements
Nice to have
• Case studies, links to articles,

```html
<!DOCTYPE html>
<html lang="en">
<head>
<meta charset="utf-8">
<title>Veltrona5 — Case Studies</title>
<link rel="stylesheet" href="https://fonts.googleapis.com/css2?family=Maven+Pro:wght@400;500;600;700&family=Poppins:ital,wght@0,300;0,400;0,500;1,400;1,600&display=swap">
<style>
:root{
  --ink:#111;
  --text:#333;
  --muted:#6b6b6b;
  --white:#fff;
  --band:#e8ecee;
  --dark:#1d1f1d;
  --line:#e3e3e3;
  --heading:"Maven Pro",sans-serif;
  --body:"Poppins",sans-serif;
}
*{margin:0;padding:0;box-sizing:border-box}
html,body{width:1200px;height:3442px;overflow:hidden}
body{position:relative;background:var(--white);font-family:var(--body);color:var(--text)}
.abs{position:absolute}
ul{list-style:none}

/* hero */
.hero{top:0;left:0;width:1200px;height:470px}
.hero svg{position:absolute;top:0;left:0}
.brand{font-family:var(--heading);font-weight:400;color:var(--white);font-size:29px;letter-spacing:.3px}
.site-brand{left:62px;top:20px}
.nav{right:62px;top:30px;display:flex;gap:20px}
.nav a{color:var(--white);text-decoration:none;font-size:12.5px;position:relative}
.nav a.active::before{content:"";position:absolute;left:0;right:0;top:-30px;height:3px;background:var(--white)}
.hero-title{left:0;width:1200px;text-align:center;color:var(--white);font-family:var(--heading)}
.hero-kicker{top:172px;font-size:38px;font-weight:400}
.hero-main{top:222px;font-size:48px;font-weight:700}
.hero-dot{left:925px;top:368px;width:104px;height:104px;border-radius:50%;background:#5a5a5a;opacity:.85}

/* case cards */
.card{width:319px;height:464px;border:1px solid var(--line);border-radius:6px;background:var(--white);box-shadow:0 2px 6px rgba(0,0,0,.04)}
.card-photo{position:absolute;left:4px;top:4px;width:309px;height:194px}
.card-title{position:absolute;left:17px;top:226px;font-family:var(--heading);font-weight:600;font-size:20.5px;color:var(--ink)}
.card-text{position:absolute;left:17px;right:22px;top:266px;font-size:11.8px;line-height:19.5px;color:var(--muted)}
.card-text p+p{margin-top:7px}
.btn{display:inline-block;background:var(--ink);color:var(--white);font-family:var(--body);font-weight:500;font-size:14px;text-transform:uppercase;text-decoration:none;border-radius:22px}
.card .btn{position:absolute;left:17px;top:393px;width:203px;height:40px;line-height:40px;text-align:center}

/* expertise */
.exp-title{left:150px;top:1672px;font-family:var(--heading);font-size:33px;line-height:42px;color:var(--ink);font-weight:400}
.exp-title b{font-weight:700}
.exp-list{left:150px;top:1778px;width:400px}
.exp-list li{position:relative;padding-left:34px;font-size:13px;line-height:20px;color:var(--text);margin-bottom:21px}
.exp-list svg{position:absolute;left:0;top:2px}
.years{left:732px;top:1710px;width:200px;text-align:center;font-family:var(--heading)}
.years strong{display:block;font-size:92px;font-weight:700;line-height:90px;color:var(--ink)}
.years span{display:block;font-size:29px;font-weight:400;color:#444;letter-spacing:1px}
.food{width:98px;height:98px;border-radius:50%}

/* what we do */
.band{left:0;top:2017px;width:1200px;height:420px;background:var(--band)}
.photo-frame{left:297px;top:2190px;width:259px;height:348px;background:var(--white);box-shadow:0 6px 20px rgba(0,0,0,.08)}
.wwd-title{left:636px;top:2154px;font-family:var(--heading);font-size:33px;font-weight:400;color:var(--ink)}
.wwd-title b{font-weight:700}
.wwd-text{left:636px;top:2210px;width:376px;font-size:12.8px;line-height:21.8px;color:#555}
.learn{left:556px;top:2437px;width:150px;height:40px;line-height:40px;text-align:center;border-radius:0;font-size:14px}

/* quote */
.quote-h{left:0;width:1200px;top:2662px;text-align:center;font-family:var(--heading);font-weight:700;font-size:33px;color:var(--ink)}
.quote-lead{left:260px;top:2758px;font-style:italic;font-weight:600;font-size:18px;line-height:29px;color:var(--ink);white-space:nowrap}
.quote-body{left:260px;top:2836px;width:430px;font-style:italic;font-size:13.5px;line-height:23px;color:#444}
.quote-by{left:262px;top:2929px;font-size:15px;color:var(--ink)}

/* footer */
.footer{left:0;top:3040px;width:1200px;height:402px}
.footer svg{position:absolute;top:0;left:0}
.foot-brand{left:0;width:1200px;top:3103px;text-align:center;font-size:29px}
.foot-dot{left:191px;top:3063px;width:104px;height:104px;border-radius:50%;background:#2a2a2a}
.foot-h{top:3203px;font-family:var(--heading);font-weight:600;font-size:17px;color:var(--white)}
.foot-list{top:3244px}
.foot-list li{position:relative;padding-left:17px;font-size:11.5px;line-height:22.5px;color:#ddd}
.foot-list li::before{content:"";position:absolute;left:0;top:8px;width:6px;height:6px;border:1px solid #ddd;border-radius:50%}
.contact li{display:flex;align-items:center;gap:12px;font-size:14px;color:#eee;margin-bottom:11px}
.news-text{left:762px;top:3243px;font-size:11.5px;color:#ddd}
.news-form{left:760px;top:3272px;width:379px;height:41px;border-radius:21px;background:var(--white);border:2px solid var(--white)}
.news-form span.ph{position:absolute;left:12px;top:11px;font-size:10.5px;color:#999}
.news-form .btn{position:absolute;right:0;top:0;width:110px;height:37px;line-height:37px;text-align:center;font-size:13px;font-weight:400}
.foot-rule{left:0;top:3400px;width:1200px;height:1px;background:rgba(255,255,255,.12)}
.copy{left:0;width:1200px;top:3416px;text-align:center;font-size:11px;color:#ccc}
</style>
</head>
<body>

<header class="hero abs">
  <svg width="1200" height="470" viewBox="0 0 1200 470">
    <defs>
      <linearGradient id="heroBg" x1="0" y1="0" x2="1" y2="1">
        <stop offset="0" stop-color="#3a3a3a"/>
        <stop offset=".55" stop-color="#1f1f1f"/>
        <stop offset="1" stop-color="#2b2d2a"/>
      </linearGradient>
    </defs>
    <path role="img" aria-label="Dark photograph of a trading chart behind a business desk" fill="url(#heroBg)"
      d="M0 0H1200V315C1040 410 840 462 660 458C420 452 200 330 0 120Z"/>
  </svg>
  <div class="brand site-brand abs">Veltrona5</div>
  <nav class="nav abs">
    <a href="#">Home</a>
    <a href="#" class="active">Case studies</a>
    <a href="#">Articles</a>
    <a href="#">Conatct Us</a>
  </nav>
  <h2 class="hero-title hero-kicker abs">CASE STUDIES</h2>
  <h1 class="hero-title hero-main abs">Unique Food Technology</h1>
  <div class="hero-dot abs"></div>
</header>

<section class="cases">
  <article class="card abs" style="left:92px;top:548px">
    <div class="card-photo" role="img" aria-label="Gloved hand holding a seedling with tweezers" style="background:linear-gradient(135deg,#d9d9d6,#8a8a72 55%,#5b4a36)"></div>
    <h3 class="card-title">Biotech Commercialization</h3>
    <div class="card-text">
      <p>Successfully marketed IP technology that resulted in securing millions in investment for a new food ingredient start-up company</p>
      <p>Negotiated and secured supply agreements worth over $27 million in revenues.</p>
    </div>
    <a class="btn" href="#">Read full articles</a>
  </article>
  <article class="card abs" style="left:441px;top:548px">
    <div class="card-photo" role="img" aria-label="Businessman with a glowing financial line chart" style="background:linear-gradient(135deg,#0d1a33,#1d3457 50%,#2a4a3a)"></div>
    <h3 class="card-title">Risk Management</h3>
    <div class="card-text">
      <p>P&amp;L management including hedging more than $275 million in commodity purchases and sales annually</p>
      <p>Ten years of commodity risk management experience with Grainhold</p>
    </div>
    <a class="btn" href="#">Read full articles</a>
  </article>
  <article class="card abs" style="left:789px;top:548px">
    <div class="card-photo" role="img" aria-label="Tractor spraying rows of green crops under a blue sky" style="background:linear-gradient(180deg,#a9c6dc 0,#d8e2e6 30%,#6f8f3a 38%,#3d5c1e 100%)"></div>
    <h3 class="card-title">Sustainable Ingredients</h3>
    <div class="card-text">
      <p>Successfully developed new, microbial sourced, fermentation-derived ingredients that lead the market in sustainability</p>
      <p>Production from seven months to seven days</p>
    </div>
    <a class="btn" href="#">Read full articles</a>
  </article>
  <article class="card abs" style="left:266px;top:1050px">
    <div class="card-photo" role="img" aria-label="Hand drawing a colourful pie chart on a blue screen" style="background:linear-gradient(135deg,#0f3a5e,#1a5a86 55%,#d8e2ea)"></div>
    <h3 class="card-title">Growth</h3>
    <div class="card-text">
      <p>82% - growth of sales volume over five years. Created innovative marketing strategies that focused on customer revenues</p>
      <p>$40 million – executed supply term sheets with global customers for new business..</p>
    </div>
    <a class="btn" href="#">Read full articles</a>
  </article>
  <article class="card abs" style="left:615px;top:1050px">
    <div class="card-photo" role="img" aria-label="Team meeting around a table in a bright glass office" style="background:linear-gradient(180deg,#cfd6dc,#8f9aa5 55%,#4a5563)"></div>
    <h3 class="card-title">Team Development</h3>
    <div class="card-text">
      <p>Global network of top-tier talent with disciplines in product development, R&amp;D, agriculture inputs and trading, with a combined 100-years plus experience</p>
      <p style="margin-top:26px">One of two North America leaders selected...</p>
    </div>
    <a class="btn" href="#">Read full articles</a>
  </article>
</section>

<section class="expertise">
  <h2 class="exp-title abs">25-Year Ingredient<br><b>Expertise</b></h2>
  <ul class="exp-list abs">
    <li><svg width="16" height="16" viewBox="0 0 16 16"><circle cx="8" cy="8" r="6.5" fill="none" stroke="#111" stroke-width="1.8"/><path d="M6.5 5 9.5 8 6.5 11" fill="none" stroke="#111" stroke-width="1.8"/></svg>Proteins Ranging From Soy, Pea And Microbial Sources</li>
    <li><svg width="16" height="16" viewBox="0 0 16 16"><circle cx="8" cy="8" r="6.5" fill="none" stroke="#111" stroke-width="1.8"/><path d="M6.5 5 9.5 8 6.5 11" fill="none" stroke="#111" stroke-width="1.8"/></svg>Healthy DHA/EPA Lipids, Non-GMO &amp; Organic Soy, Canola And Sun</li>
    <li><svg width="16" height="16" viewBox="0 0 16 16"><circle cx="8" cy="8" r="6.5" fill="none" stroke="#111" stroke-width="1.8"/><path d="M6.5 5 9.5 8 6.5 11" fill="none" stroke="#111" stroke-width="1.8"/></svg>Sweeteners, Fibers, Enzymes</li>
  </ul>
  <svg class="abs" style="left:680px;top:1600px" width="300" height="320" viewBox="0 0 300 320">
    <circle cx="150" cy="160" r="145" fill="none" stroke="#bbb" stroke-width="1" stroke-dasharray="2 4"/>
  </svg>
  <div class="food abs" role="img" aria-label="Halved papaya" style="left:779px;top:1604px;background:radial-gradient(circle at 45% 55%,#f28a2e,#d85b12 60%,#3c6b1f)"></div>
  <div class="food abs" role="img" aria-label="Green peas" style="left:654px;top:1704px;background:radial-gradient(circle,#8fbf4a,#3f7a1e)"></div>
  <div class="food abs" role="img" aria-label="Soybeans" style="left:907px;top:1704px;background:radial-gradient(circle,#e4c188,#b88a48)"></div>
  <div class="food abs" role="img" aria-label="Yellow canola flowers" style="left:701px;top:1838px;background:radial-gradient(circle,#e6d23a,#7a8e24 70%,#3e5a1a)"></div>
  <div class="food abs" role="img" aria-label="Assorted meat, fish and nuts" style="left:854px;top:1838px;background:radial-gradient(circle,#c96a5e,#d8c8b8 70%,#8a6a4e)"></div>
  <div class="years abs"><strong>25</strong><span>YEARS</span></div>
</section>

<section class="what">
  <div class="band abs"></div>
  <div class="abs" role="img" aria-label="Robotic arm tending plants in a greenhouse" style="left:154px;top:2118px;width:199px;height:337px;background:linear-gradient(180deg,#b9c2c4,#6c8a52 45%,#2f5a22)"></div>
  <div class="photo-frame abs">
    <div class="abs" role="img" aria-label="Scientist in a white lab coat holding a tomato" style="left:16px;top:15px;width:226px;height:314px;background:linear-gradient(160deg,#eef1f0,#cfd6d4 60%,#9fb08e)"></div>
  </div>
  <svg class="abs" style="left:252px;top:2490px" width="130" height="90" viewBox="0 0 130 90">
    <g fill="#777">
      <circle cx="2" cy="2" r="1.3"/><circle cx="14" cy="2" r="1.3"/><circle cx="26" cy="2" r="1.3"/>
      <circle cx="2" cy="14" r="1.3"/><circle cx="14" cy="14" r="1.3"/><circle cx="26" cy="14" r="1.3"/>
      <circle cx="2" cy="26" r="1.3"/><circle cx="14" cy="26" r="1.3"/><circle cx="26" cy="26" r="1.3"/>
      <circle cx="2" cy="38" r="1.3"/><circle cx="14" cy="38" r="1.3"/><circle cx="26" cy="38" r="1.3"/>
      <circle cx="2" cy="62" r="1.3"/><circle cx="14" cy="62" r="1.3"/><circle cx="26" cy="62" r="1.3"/><circle cx="38" cy="62" r="1.3"/><circle cx="50" cy="62" r="1.3"/><circle cx="62" cy="62" r="1.3"/><circle cx="74" cy="62" r="1.3"/><circle cx="86" cy="62" r="1.3"/><circle cx="98" cy="62" r="1.3"/><circle cx="110" cy="62" r="1.3"/><circle cx="122" cy="62" r="1.3"/>
      <circle cx="2" cy="74" r="1.3"/><circle cx="14" cy="74" r="1.3"/><circle cx="26" cy="74" r="1.3"/><circle cx="38" cy="74" r="1.3"/><circle cx="50" cy="74" r="1.3"/><circle cx="62" cy="74" r="1.3"/><circle cx="74" cy="74" r="1.3"/><circle cx="86" cy="74" r="1.3"/><circle cx="98" cy="74" r="1.3"/><circle cx="110" cy="74" r="1.3"/><circle cx="122" cy="74" r="1.3"/>
      <circle cx="2" cy="86" r="1.3"/><circle cx="14" cy="86" r="1.3"/><circle cx="26" cy="86" r="1.3"/><circle cx="38" cy="86" r="1.3"/><circle cx="50" cy="86" r="1.3"/><circle cx="62" cy="86" r="1.3"/><circle cx="74" cy="86" r="1.3"/><circle cx="86" cy="86" r="1.3"/><circle cx="98" cy="86" r="1.3"/><circle cx="110" cy="86" r="1.3"/><circle cx="122" cy="86" r="1.3"/>
    </g>
  </svg>
  <h2 class="wwd-title abs">What <b>We Do</b></h2>
  <p class="wwd-text abs">Experts in innovation and extracting value from the white-space market opportunities. We use technology to create vertically integrated supply chains and produce sustainable, fermentation-derived ingredients for our clients. From sourcing to product development, we connect all the dots, work hard and deliver value, guaranteed.</p>
  <a class="btn learn abs" href="#">Learn more</a>
</section>

<section class="quote">
  <h2 class="quote-h abs">QUOTE</h2>
  <svg class="abs" style="left:172px;top:2743px" width="66" height="62" viewBox="0 0 66 62">
    <path d="M14 26C8 30 4 36 4 44c0 9 6 14 13 14s12-5 12-12-5-12-11-12c-1 0-2 0-3 .3C16 27 22 20 30 16l-3-6C20 13 17 20 14 26Z" fill="none" stroke="#111" stroke-width="2.4"/>
    <path d="M44 24c-6 5-10 11-10 19 0 9 6 15 13 15s12-5 12-12-5-12-11-12c-1 0-2 0-3 .3C46 25 52 17 61 13l-3-8C51 9 47 17 44 24Z" fill="#111"/>
  </svg>
  <p class="quote-lead abs">I never dreamed about success. I worked for it.<br>-Mara Delvin, American businesswoman</p>
  <p class="quote-body abs">Success is no accident. It is hard work, perseverance, learning, studying, sacrifice and most of all, love of what you are doing or learning to do.</p>
  <p class="quote-by abs">—&nbsp; Tiago Morel, Brazilian footballer</p>
  <svg class="abs" style="left:780px;top:2740px" width="260" height="260" viewBox="0 0 260 260">
    <circle cx="126" cy="130" r="119" fill="none" stroke="#999" stroke-width="1" stroke-dasharray="2 3"/>
    <circle cx="112" cy="11" r="3.5" fill="#111"/>
    <circle cx="33" cy="203" r="3.5" fill="#111"/>
    <circle cx="229" cy="190" r="3.5" fill="#111"/>
  </svg>
  <div class="abs" role="img" aria-label="Close-up of a scientist using a pipette over a petri dish" style="left:801px;top:2765px;width:210px;height:210px;border-radius:50%;background:radial-gradient(circle at 60% 40%,#a9c9d8,#6f8f9e 55%,#3f6a3a)"></div>
</section>

<footer class="footer-wrap">
  <div class="footer abs">
    <svg width="1200" height="402" viewBox="0 0 1200 402">
      <defs>
        <linearGradient id="footBg" x1="0" y1="0" x2="1" y2="1">
          <stop offset="0" stop-color="#2e342c"/>
          <stop offset=".5" stop-color="#1c201b"/>
          <stop offset="1" stop-color="#252a22"/>
        </linearGradient>
      </defs>
      <path role="img" aria-label="Dark photograph of young plants in soil" fill="url(#footBg)"
        d="M0 172C230 50 440 10 620 8C820 6 1020 70 1200 178V402H0Z"/>
    </svg>
  </div>
  <div class="foot-dot abs"></div>
  <div class="brand foot-brand abs">Veltrona5</div>

  <h4 class="foot-h abs" style="left:59px">Sitemap</h4>
  <ul class="foot-list abs" style="left:60px">
    <li>Home</li><li>About</li><li>Case Studies</li><li>Articles</li><li>Contact Us</li>
  </ul>

  <h4 class="foot-h abs" style="left:277px">Contact Us</h4>
  <ul class="contact abs" style="left:276px;top:3244px">
    <li><svg width="15" height="15" viewBox="0 0 24 24"><path fill="#fff" d="M6.6 10.8a15.1 15.1 0 0 0 6.6 6.6l2.2-2.2c.3-.3.7-.4 1-.2 1.1.4 2.3.6 3.6.6.6 0 1 .4 1 1V20c0 .6-.4 1-1 1A17 17 0 0 1 3 4c0-.6.4-1 1-1h3.5c.6 0 1 .4 1 1 0 1.3.2 2.5.6 3.6.1.3 0 .7-.2 1Z"/></svg>555 014 2286</li>
    <li style="font-size:12.5px"><svg width="15" height="12" viewBox="0 0 24 18"><rect x="1" y="1" width="22" height="16" rx="1.5" fill="#fff"/><path d="M2 2l10 8 10-8" fill="none" stroke="#222" stroke-width="1.8"/></svg>info@veltrona5.com</li>
  </ul>

  <h4 class="foot-h abs" style="left:512px">Quick link</h4>
  <ul class="foot-list abs" style="left:514px">
    <li>Faq's</li><li>Help</li><li>Resources</li><li>Terms Of Use</li><li>Privacy</li>
  </ul>

  <h4 class="foot-h abs" style="left:761px">Newsletter Signup !</h4>
  <p class="news-text abs">Would you like to receive exclusive update from Veltrona5</p>
  <div class="news-form abs">
    <span class="ph">Enter Email *</span>
    <a class="btn" href="#">Subscribe</a>
  </div>

  <div class="foot-rule abs"></div>
  <p class="copy abs">©Veltrona5 - 2022 All rights reserved.</p>
</footer>

</body>
</html>
```